Seattle Area Commercial Real Estate Marketing Flyer Template

We need a flyer template to use for marketing available commercial real estate space through our portfolio. Looking for a template that works with our overall brand and allows us to add in text and photos for the specific space. Attached is a draft flyer that we have been using that reflects the info/photos we will need to be able to input. We would like to see designs that use a similar design to our website at trvb.com and use our attached logo.

Target Market(s)

Tenants looking for office space

Font styles to use
Sans Serif

Colors
9bcb3c
ffffff

Requirements
Must have
• Areas to insert text and photos
• Company Logo

```html
<!DOCTYPE html>
<html lang="en">
<head>
<meta charset="utf-8">
<title>Tall River Bay Partners — Flyer Set</title>
<link href="https://fonts.googleapis.com/css2?family=Libre+Baskerville:wght@400;700&family=Montserrat:wght@400;600;700&display=swap" rel="stylesheet">
<style>
:root{
  --green:#8dbb2a;
  --green-bright:#9bcb3c;
  --ink:#2a2a2a;
  --panel:#2b2b2b;
  --stage:#595959;
  --paper:#ffffff;
  --muted:#d9d9d9;
  --text:#3a3a3a;
}
*{box-sizing:border-box;margin:0;padding:0}
html,body{width:1200px;height:1200px;overflow:hidden;background:var(--stage)}
body{position:relative;font-family:"Montserrat",sans-serif;color:var(--text)}
.page{position:absolute;width:419px;height:539px;background:var(--paper);overflow:hidden}
.page--stewardship{left:141px;top:38px}
.page--cover{left:628px;top:38px}
.page--about{left:141px;top:616px}
.page--portfolio{left:628px;top:616px}
.abs{position:absolute}
.photo{position:absolute}
.serif{font-family:"Libre Baskerville",serif}
.section-title{position:absolute;font-family:"Libre Baskerville",serif;font-weight:700;font-size:12px;color:var(--ink);padding-left:9px;border-left:4px solid var(--green);line-height:17px;letter-spacing:.2px}
.body-copy{font-size:7.3px;line-height:9.6px;color:var(--text)}
.justify{text-align:justify}

/* page 1 */
.house-photo{left:0;top:0;width:419px;height:260px;background:linear-gradient(180deg,#6fa3d8 0%,#bcd6ee 25%,#e6dcc4 42%,#cfc6ad 58%,#7c9a5a 72%,#c9d6b8 86%,#ffffff 100%)}
.partner{position:absolute;top:312px;width:150px;text-align:center}
.partner__name{font-size:11px;font-weight:700;display:inline-flex;align-items:center;gap:5px}
.partner__name i{display:inline-block;width:10px;height:10px;border-radius:50%}
.partner__text{margin-top:9px;font-size:7.3px;line-height:9.6px}
.contact{left:0;top:398px;width:419px;height:141px;background:var(--panel);color:#e8e8e8;font-size:7.3px;line-height:9.5px}
.contact h3{position:absolute;left:32px;top:14px;font-size:11.5px;font-weight:700;color:var(--green)}
.contact .col{position:absolute;top:48px}
.contact p{margin-bottom:6.5px}
.follow{display:flex;align-items:center;gap:8px}
.follow i{width:10px;height:10px;border-radius:50%;background:var(--green)}

/* page 2 */
.brand{position:absolute;left:0;top:38px;width:419px;text-align:center;font-size:10.5px;color:#555;display:flex;justify-content:center;align-items:center;gap:7px}
.brand i{width:18px;height:18px;background:var(--green-bright)}
.cover-kicker{position:absolute;left:0;top:94px;width:419px;text-align:center;font-family:"Libre Baskerville",serif;font-weight:700;font-size:15px;color:var(--ink)}
.cover-title{position:absolute;left:0;top:112px;width:419px;text-align:center;font-family:"Libre Baskerville",serif;font-weight:700;font-size:31px;color:var(--green);letter-spacing:.3px}
.cover-sub{position:absolute;left:0;top:145px;width:419px;text-align:center;font-family:"Libre Baskerville",serif;font-weight:700;font-size:13.6px;color:var(--green)}
.address-bar{position:absolute;left:65px;top:172px;width:290px;height:18px;background:var(--panel);color:var(--green-bright);font-size:6px;font-weight:600;display:flex;align-items:center;justify-content:center;gap:8px}
.address-bar span+span{border-left:1px solid var(--green-bright);padding-left:8px}
.building-photo{left:0;top:160px;width:419px;height:379px;background:linear-gradient(180deg,#ffffff 0%,#cfe2f5 12%,#8fb8e2 26%,#d8c9a0 42%,#c8b98f 60%,#4f7a3a 76%,#8a8a82 90%,#a09e96 100%)}

/* page 3 */
.crew-photo{left:12px;top:0;width:190px;height:194px;background:linear-gradient(180deg,#7fb0e6 0%,#c8a24a 40%,#9a8f7a 70%,#6d5a43 100%)}
.rule{position:absolute;left:222px;top:64px;width:58px;height:2px;background:var(--green)}
.intro{left:222px;top:72px;width:180px}
.history{left:0;top:199px;width:419px;height:111px;background:var(--panel);color:#eee;padding:19px 19px 0}
.history p{margin-bottom:6px}
.headshot{left:19px;top:338px;width:115px;height:140px;background:linear-gradient(180deg,#c7cfd6 0%,#b9a595 55%,#2f3442 100%)}
.team{left:237px;top:374px;font-size:7.3px;line-height:16px;color:var(--ink)}
.team b{font-weight:700}
.footer-bar{position:absolute;left:12px;top:507px;width:396px;height:19px;background:var(--green);color:#fff;font-size:10.5px;letter-spacing:1.6px;display:flex;align-items:center;justify-content:center}

/* page 4 */
.courtyard-photo{left:12px;top:12px;width:130px;height:490px;background:linear-gradient(180deg,#ffffff 0%,#ece7dc 30%,#d6cbb6 55%,#6d5b45 70%,#b7ab97 85%,#d9d0c1 100%)}
.reasons{left:198px;width:200px}
.stats{left:156px;top:270px;width:252px;height:230px;background:var(--panel)}
.stat{position:absolute;top:32px;text-align:center;color:#fff;font-family:"Libre Baskerville",serif;font-weight:700;font-size:6.8px}
.stat b{display:block;color:var(--green-bright);font-size:23px;line-height:26px}
.us-map{left:18px;top:88px;width:220px;height:126px;background:linear-gradient(160deg,#f2f2f2,#dcdcdc);border-radius:14px 26px 30px 16px}
</style>
</head>
<body>

<!-- Stewardship & contact -->
<section class="page page--stewardship">
  <div class="photo house-photo" role="img" aria-label="Photo of a modern single-storey home with garden under a blue sky"></div>
  <h2 class="section-title" style="left:19px;top:231px">COMMUNITY STEWARDSHIP</h2>
  <p class="abs body-copy justify" style="left:29px;top:262px;width:362px">Stewardship is part of our culture and reflects our commitment to investing in the community in which we work. While we build projects in our community, we also build relationships that help support important non-profit organizations.</p>
  <div class="partner" style="left:23px">
    <div class="partner__name" style="color:#d2232a"><i style="background:#d2232a"></i>Harbor Kids Closet</div>
    <p class="partner__text">Giving kids the essentials that they need to thrive by providing food, clothing and beds.</p>
  </div>
  <div class="partner" style="left:253px;width:140px">
    <div class="partner__name" style="color:#6a2c8e"><i style="background:#6a2c8e"></i>Brightpath</div>
    <p class="partner__text">Embracing children by providing education and therapies to nurture hope, courage and the skills to soar</p>
  </div>
  <div class="abs contact">
    <h3>CONTACT US</h3>
    <div class="col" style="left:32px">
      <p>TALL RIVER BAY PARTNERS<br>4410 NE Cedar Ridge Road, Suite 210<br>Redmond, WA 98052</p>
      <p>info@trvb.com</p>
      <p>(206) 555-0148</p>
      <p>www.trvb.com</p>
    </div>
    <div class="col" style="left:287px">
      <p>LEASING<br>leasing@trvb.com</p>
      <p>PROPERTY MANAGEMENT<br>property@trvb.com</p>
      <p class="follow">FOLLOW US <i></i></p>
    </div>
  </div>
</section>

<!-- Cover -->
<section class="page page--cover">
  <div class="photo building-photo" role="img" aria-label="Photo of a modern beige brick office building with landscaped garden"></div>
  <div class="brand"><i></i>Tall River Bay Partners</div>
  <p class="cover-kicker">IT STARTS WITH</p>
  <h1 class="cover-title">GREAT BUILDINGS</h1>
  <p class="cover-sub">AND ENDS WITH GREAT TENANTS</p>
  <div class="address-bar"><span>4410 NE Cedar Ridge Road, Suite 210 Redmond, WA 98052</span><span>www.trvb.com</span></div>
</section>

<!-- About & team -->
<section class="page page--about">
  <div class="photo crew-photo" role="img" aria-label="Photo of three partners at a groundbreaking in front of a bulldozer"></div>
  <div class="rule"></div>
  <p class="abs body-copy justify intro"><b>Tall River Bay Partners</b> is a privately owned commercial real estate company. Our focus is on long-term portfolio investments and development projects across the country. We specialize in large-scale industrial facilities and Class A office space.</p>
  <div class="abs body-copy history">
    <p>Evan Marsh, our president and founder, was influenced and encouraged by his late grandfather, Leo Marsh. Leo was an entrepreneur, community leader, and investor in some of Seattle's most iconic real estate, including the Meridian Building, a downtown Seattle landmark. Evan's early experiences and his growing interest in commercial real estate fueled him to create Tall River Bay Partners.</p>
    <p>Under Evan's leadership, Tall River Bay Partners has successfully developed and acquired 7-million square feet of property nationwide, with more than 1-million in the Seattle metro area... and we continue to grow.</p>
  </div>
  <div class="photo headshot" role="img" aria-label="Portrait photo of the principal"></div>
  <h2 class="section-title" style="left:199px;top:346px">THE TEAM</h2>
  <ul class="abs team" style="list-style:none">
    <li><b>EVAN MARSH,</b> Principal</li>
    <li><b>PAUL AVERY,</b> Sr. Construction Manager</li>
    <li><b>SEAN DOYLE,</b> Controller</li>
    <li><b>LAURA FINCH,</b> Sr. Property Manager</li>
    <li><b>MEGAN HALE,</b> Business Operations Manager</li>
    <li><b>DANA PRYOR,</b> Sr. Accountant</li>
    <li><b>NADIA KARIMI,</b> Counsel</li>
  </ul>
  <div class="footer-bar">www.trvb.com</div>
</section>

<!-- Why & portfolio -->
<section class="page page--portfolio">
  <div class="photo courtyard-photo" role="img" aria-label="Photo of a white stucco outdoor fireplace in a patio courtyard"></div>
  <h2 class="section-title" style="left:154px;top:14px">WHY WE'RE DIFFERENT</h2>
  <p class="abs body-copy reasons" style="top:60px">We own every building we operate and we operate every building we own.</p>
  <p class="abs body-copy reasons" style="top:102px">We are customer-centric, fostering strong professional relationships with our clients.</p>
  <p class="abs body-copy reasons" style="top:143px">We are more than just buildings. We are long-term investors in our properties and our communities.</p>
  <p class="abs body-copy reasons" style="top:185px">We are privately-held, which allows us to always put our clients' needs first.</p>
  <h2 class="section-title" style="left:154px;top:237px">OUR PORTFOLIO</h2>
  <div class="abs stats">
    <div class="stat" style="left:20px;width:70px"><b>23</b>PROPERTIES</div>
    <div class="stat" style="left:104px;width:50px"><b>9</b>STATES</div>
    <div class="stat" style="left:158px;width:90px"><b>8</b>MILLION SQ. FT.</div>
    <div class="abs us-map" role="img" aria-label="Map of the United States with pins marking portfolio cities from Seattle to Jacksonville"></div>
  </div>
  <div class="footer-bar">www.trvb.com</div>
</section>

</body>
</html>
```